Kettle Wyldz Web Design Theme Ideas

I have a new golf website that I am designing. It will be a website where a group of golfers can track their scores and results as a small tournament. The site will allow side matches between players. These players are referred to as "Pigeons". The side matches are what I refer to as "Chaos". But, I would rather spell it "Wyldz". Looking for some good ideas for a crazy looking pigeon themed golfer. The definition of a "pigeon" in golf is a golfer who is not that good but thinks they are good. Obviously, "chaos" is disorderly confusion.

Target Market(s)

Golfers who like to gamble with other golfers

Industry/Entity Type

Golf

Number of Pages Required

5+ page

Font styles to use
Sans Serif

Requirements
Must have
• Pigeons, golf theme
Should not have
• the words gamble, bet, wager

```html
<!DOCTYPE html>
<html lang="en">
<head>
<meta charset="utf-8">
<title>Kettle Wyldz</title>
<link href="https://fonts.googleapis.com/css2?family=Montserrat:wght@400;500;600;700&family=Oswald:wght@500;600&display=swap" rel="stylesheet">
<style>
:root{
  --green:#4a8c2a;
  --green-dark:#16301f;
  --navy:#0c2130;
  --ink:#1b1b1b;
  --muted:#555;
  --card:#e1eef6;
  --line:#e4e4e4;
  --ghost:#ececec;
}
*{margin:0;padding:0;box-sizing:border-box}
html,body{width:1200px;height:3563px;overflow:hidden;background:#fff}
body{position:relative;font-family:'Montserrat',sans-serif;color:var(--ink)}
.abs{position:absolute}
.heading{font-family:'Oswald',sans-serif;font-weight:500;font-size:46px;letter-spacing:.5px;text-transform:uppercase;color:var(--navy);text-align:center;left:0;width:1200px;line-height:1}
.heading span{color:var(--green)}
.ghost{font-family:'Montserrat',sans-serif;font-weight:600;text-align:center;left:0;width:1200px;color:transparent;-webkit-text-stroke:1.5px var(--ghost);line-height:1;white-space:nowrap}
.btn{display:flex;align-items:center;justify-content:center;border-radius:30px;background:linear-gradient(90deg,#3e8a2a,#123024);color:#fff;font-weight:600;font-size:15px}
.brand{font-family:'Oswald',sans-serif;font-weight:600;font-size:28px;letter-spacing:.3px;display:flex;align-items:center;gap:8px}
.brand i{display:block;width:14px;height:14px;border-radius:50%;background:var(--green)}

/* nav */
.nav a{position:absolute;top:40px;font-size:15.5px;color:#444;text-decoration:none}
.nav a.active{color:var(--green);font-weight:500}

/* hero */
.hero{left:0;top:101px;width:1200px;height:470px;border-radius:22px;background:linear-gradient(180deg,#b9cdd2 0%,#cfd9c8 45%,#7fa44a 70%,#5b8a2c 100%)}
.hero-ghost{font-family:'Montserrat',sans-serif;font-weight:700;font-size:120px;color:rgba(255,255,255,.18);line-height:1}

/* about */
.about-text p{font-size:15.5px;line-height:30px;text-align:justify;color:#333;margin-bottom:8px}

/* table */
.table{left:111px;top:1305px;width:977px;height:344px;border:1px solid var(--line);border-radius:8px;overflow:hidden}
.thead{height:53px;background:var(--navy);color:#fff;font-size:19px;position:relative}
.thead span,.row span{position:absolute;top:50%;transform:translateY(-50%)}
.row{height:57.4px;border-bottom:1px solid var(--line);position:relative;font-size:17px;color:#222}
.row:last-child{border-bottom:none}
.avatar{width:40px;height:40px;border-radius:50%;background:linear-gradient(135deg,#c9a98e,#5b6f7d)}

/* side matches */
.matches{left:0;top:1776px;width:1200px;height:733px;background:var(--navy);border-radius:16px}
.match{width:441px;height:202px;background:var(--card);border-radius:12px;padding:34px 32px}
.match h3{font-size:21px;font-weight:700;color:var(--green);text-transform:uppercase}
.match .club{font-size:17px;color:#555;margin-top:8px}
.match .meta{font-size:15.5px;color:#111;margin-top:14px;padding-left:5px;line-height:31px}

/* blog */
.photo{height:250px;border-radius:4px}
.post{width:300px;height:232px;background:#fff;box-shadow:0 4px 16px rgba(0,0,0,.12);padding:28px 20px}
.post .date{font-size:14.5px;color:var(--green)}
.post h4{font-size:16px;font-weight:600;margin-top:20px}
.post p{font-size:15px;color:#444;line-height:30.5px;margin-top:10px}

/* footer */
.footer{left:0;top:3260px;width:1200px;height:303px;background:var(--navy);border-radius:16px 16px 0 0;color:#fff}
.footer h5{font-family:'Oswald',sans-serif;font-weight:500;font-size:17px;text-transform:uppercase}
.footer .links div{font-size:15.5px;line-height:30px}
.social{width:28px;height:28px;border:1.5px solid #fff;border-radius:50%}
.contact-item{display:flex;gap:14px;font-size:15.5px;line-height:28px}
.contact-item svg{flex:none;margin-top:6px}
</style>
</head>
<body>

<!-- header -->
<div class="abs brand" style="left:111px;top:30px;color:var(--navy)"><i></i>KETTLE WYLDZ</div>
<nav class="nav">
  <a class="active" style="left:435px">Home</a>
  <a style="left:507px">About</a>
  <a style="left:579px">Scores &amp; Results</a>
  <a style="left:729px">Side Matches</a>
  <a style="left:856px">Contact</a>
</nav>
<div class="abs btn" style="left:953px;top:25px;width:135px;height:47px">Register</div>

<!-- hero -->
<div class="abs hero" role="img" aria-label="Two golfers carrying bags across a sunlit fairway"></div>
<div class="abs hero-ghost" style="left:610px;top:200px">KETTLE</div>
<div class="abs" style="left:666px;top:254px;color:#fff;font-weight:600;font-size:26px">WELCOME TO</div>
<div class="abs" style="left:666px;top:288px;color:#fff;font-weight:700;font-size:52px;line-height:1.1">KETTLE WYLDZ</div>
<div class="abs btn" style="left:666px;top:368px;width:133px;height:44px">Learn More</div>

<!-- about -->
<div class="abs ghost" style="top:605px;font-size:100px">ABOUT US</div>
<div class="abs heading" style="top:658px">About <span>Us</span></div>
<div class="abs about-text" style="left:111px;top:745px;width:474px">
  <p>Lorem ipsum dolor sit amet, consectetur adipiscing elit, sed do eiusmod tempor incididunt ut labore et dolore magna aliqua. Quis ipsum suspendisse ultrices gravida. Risus com modo viverra maecenas accumsan lacus vel facilisis.</p>
  <p>Consectetur adipiscing elit, sed do eiusmod tempor incidi dunt ut labore edolore magna aliqua. Quis ipsum suspendisse ultrices gravida. Risus com modo viverra maecenas accumsan lacus vel facilisis.</p>
</div>
<div class="abs btn" style="left:111px;top:1016px;width:135px;height:46px">Learn More</div>
<div class="abs" style="left:732px;top:707px;width:356px;height:356px;border-radius:50%;background:#eef4e6"></div>
<div class="abs" role="img" aria-label="Golfer in a light blue shirt finishing his swing" style="left:762px;top:736px;width:326px;height:326px;border-radius:50%;background:linear-gradient(180deg,#5c8fc0 0%,#8fb3d4 50%,#5d7d3b 100%)"></div>
<div class="abs" role="img" aria-label="Faint pigeon decoration" style="left:1082px;top:1008px;width:92px;height:112px;border-radius:50%;background:#e3e7ee"></div>

<!-- scores -->
<div class="abs ghost" style="top:1148px;font-size:100px">Scores &amp; Results</div>
<div class="abs heading" style="top:1198px">Scores <span>&amp; Results</span></div>
<div class="abs table">
  <div class="thead">
    <span style="left:96px">RANK</span><span style="left:214px">PLAYER</span><span style="left:513px">AVERAGE POINTS</span><span style="left:783px">TOTAL POINTS</span>
  </div>
  <div class="row"><span style="left:28px"><svg width="26" height="20" viewBox="0 0 26 20" fill="none" stroke="#333" stroke-width="1.6"><path d="M2 12 C8 8 14 10 18 4 L24 3 L20 7 C20 14 12 18 4 16 Z"/><path d="M8 11 L4 4 L12 9"/></svg></span><span style="left:96px">1</span><span style="left:214px" class="avatar" role="img" aria-label="Player portrait"></span><span style="left:279px">Lorem Ipsum</span><span style="left:584px">3.25</span><span style="left:833px">35.25</span></div>
  <div class="row"><span style="left:28px"><svg width="26" height="20" viewBox="0 0 26 20" fill="none" stroke="#333" stroke-width="1.6"><path d="M2 12 C8 8 14 10 18 4 L24 3 L20 7 C20 14 12 18 4 16 Z"/><path d="M8 11 L4 4 L12 9"/></svg></span><span style="left:96px">2</span><span style="left:214px" class="avatar" role="img" aria-label="Player portrait"></span><span style="left:279px">Lorem Ipsum</span><span style="left:584px">6.0</span><span style="left:833px">61.0</span></div>
  <div class="row"><span style="left:28px"><svg width="26" height="20" viewBox="0 0 26 20" fill="none" stroke="#333" stroke-width="1.6"><path d="M2 12 C8 8 14 10 18 4 L24 3 L20 7 C20 14 12 18 4 16 Z"/><path d="M8 11 L4 4 L12 9"/></svg></span><span style="left:96px">3</span><span style="left:214px" class="avatar" role="img" aria-label="Player portrait"></span><span style="left:279px">Lorem Ipsum</span><span style="left:584px">5.26</span><span style="left:833px">65.26</span></div>
  <div class="row"><span style="left:28px"><svg width="26" height="20" viewBox="0 0 26 20" fill="none" stroke="#333" stroke-width="1.6"><path d="M2 12 C8 8 14 10 18 4 L24 3 L20 7 C20 14 12 18 4 16 Z"/><path d="M8 11 L4 4 L12 9"/></svg></span><span style="left:96px">4</span><span style="left:214px" class="avatar" role="img" aria-label="Player portrait"></span><span style="left:279px">Lorem Ipsum</span><span style="left:584px">8.0</span><span style="left:833px">78.0</span></div>
  <div class="row"><span style="left:28px"><svg width="26" height="20" viewBox="0 0 26 20" fill="none" stroke="#333" stroke-width="1.6"><path d="M2 12 C8 8 14 10 18 4 L24 3 L20 7 C20 14 12 18 4 16 Z"/><path d="M8 11 L4 4 L12 9"/></svg></span><span style="left:96px">5</span><span style="left:214px" class="avatar" role="img" aria-label="Player portrait"></span><span style="left:279px">Lorem Ipsum</span><span style="left:584px">4.11</span><span style="left:833px">84.11</span></div>
</div>
<div class="abs btn" style="left:532px;top:1678px;width:135px;height:46px">View All</div>

<!-- side matches -->
<div class="abs matches"></div>
<div class="abs" role="img" aria-label="Faint pigeon decoration" style="left:26px;top:1800px;width:88px;height:108px;border-radius:50%;background:#b9c2cf"></div>
<div class="abs ghost" style="top:1828px;font-size:108px;-webkit-text-stroke:1.5px #26394a">Side Matches</div>
<div class="abs heading" style="top:1885px;color:#fff">Side Matches</div>
<div class="abs match" style="left:144px;top:2007px"><h3>Ridgeway Open</h3><div class="club">Pinecrest Golf Club, USA</div><div class="meta">DATE: 06 - 09 Apr<br>CHAMPION: Dale Hartwick (D)</div></div>
<div class="abs match" style="left:615px;top:2007px"><h3>Ridgeway Open</h3><div class="club">Pinecrest Golf Club, USA</div><div class="meta">DATE: 06 - 09 Apr<br>CHAMPION: Dale Hartwick (D)</div></div>
<div class="abs match" style="left:144px;top:2235px"><h3>Ridgeway Open</h3><div class="club">Pinecrest Golf Club, USA</div><div class="meta">DATE: 06 - 09 Apr<br>CHAMPION: Dale Hartwick (D)</div></div>
<div class="abs match" style="left:615px;top:2235px"><h3>Ridgeway Open</h3><div class="club">Pinecrest Golf Club, USA</div><div class="meta">DATE: 06 - 09 Apr<br>CHAMPION: Dale Hartwick (D)</div></div>

<!-- blog -->
<div class="abs ghost" style="top:2570px;font-size:100px">Our Blog</div>
<div class="abs" role="img" aria-label="Faint pigeon decoration" style="left:1062px;top:2570px;width:90px;height:108px;border-radius:50%;background:#dfe4ea"></div>
<div class="abs heading" style="top:2622px">Our <span>Blog</span></div>

<div class="abs photo" role="img" aria-label="Golfer chipping out of a sand bunker" style="left:113px;top:2717px;width:317px;background:linear-gradient(180deg,#3f6a2c,#d8d6cc 60%,#8fae4a)"></div>
<div class="abs photo" role="img" aria-label="Group of friends walking the course at sunset" style="left:442px;top:2717px;width:317px;background:linear-gradient(180deg,#d2d6c8,#6f8a4a 60%,#384a2c)"></div>
<div class="abs photo" role="img" aria-label="Two golfers chatting beside a bag of clubs" style="left:771px;top:2717px;width:317px;background:linear-gradient(135deg,#4a6f95,#a9c2d6 50%,#1f2a33)"></div>

<div class="abs post" style="left:123px;top:2948px"><div class="date">04-04-2023 | By Mara Quill</div><h4>Sed ut perspiciatis unde omnis</h4><p>Sed ut perspiciatis unde omni iste natus error sit voluptate accusan tium doloremque</p></div>
<div class="abs post" style="left:452px;top:2948px"><div class="date">04-04-2023 | By Mara Quill</div><h4>Sed ut perspiciatis unde omnis</h4><p>Sed ut perspiciatis unde omni iste natus error sit voluptate accusan tium doloremque</p></div>
<div class="abs post" style="left:781px;top:2948px"><div class="date">04-04-2023 | By Mara Quill</div><h4>Sed ut perspiciatis unde omnis</h4><p>Sed ut perspiciatis unde omni iste natus error sit voluptate accusan tium doloremque</p></div>

<!-- footer -->
<footer class="abs footer">
  <div class="abs brand" style="left:111px;top:103px;color:#fff"><i></i>KETTLE WYLDZ</div>
  <div class="abs social" style="left:130px;top:164px"></div>
  <div class="abs social" style="left:165px;top:164px"></div>
  <div class="abs social" style="left:200px;top:164px"></div>
  <div class="abs social" style="left:235px;top:164px"></div>

  <h5 class="abs" style="left:395px;top:45px">Contact Us</h5>
  <div class="abs" style="left:393px;top:87px">
    <div class="contact-item"><svg width="14" height="18" viewBox="0 0 14 18"><path d="M7 0C3 0 0 3 0 7c0 5 7 11 7 11s7-6 7-11c0-4-3-7-7-7z" fill="#4a8c2a"/><circle cx="7" cy="7" r="2.5" fill="#0c2130"/></svg><div>Kettle Wyldz,<br>Address Comes Here</div></div>
    <div class="contact-item" style="margin-top:10px"><svg width="16" height="16" viewBox="0 0 16 16"><path d="M3 1l3 3-2 2c1 2 3 4 5 5l2-2 3 3-2 3C7 15 1 9 0 3z" fill="#4a8c2a"/></svg><div>+1 555-010-2040</div></div>
    <div class="contact-item" style="margin-top:12px"><svg width="16" height="12" viewBox="0 0 16 12"><rect width="16" height="12" rx="1" fill="#4a8c2a"/><path d="M1 1l7 6 7-6" stroke="#0c2130" stroke-width="1.4" fill="none"/></svg><div>info@kettlewyldz.com</div></div>
  </div>

  <h5 class="abs" style="left:704px;top:45px">Quick Links</h5>
  <div class="abs links" style="left:704px;top:85px"><div>Home</div><div>About</div><div>Scores &amp; Results</div><div>Side Matches</div></div>

  <h5 class="abs" style="left:937px;top:45px">Other Links</h5>
  <div class="abs links" style="left:937px;top:85px"><div>Contact</div><div>Terms &amp; Conditions</div><div>Privacy Policy</div><div>Cookies</div></div>

  <div class="abs" style="left:0;width:1200px;top:258px;text-align:center;font-size:14.5px">2023 Kettle Wyldz. All Rights Reserved.</div>
</footer>

</body>
</html>
```